Loose Saltbush Venture

I am creating a personal blog to outline, in pictures and words, the cultural decay of everyday life in Australia today. This has been manifested by the rise of a nanny state.
Australia's foundation was based on hardened men i.e.- convicts, lifeguards, determined, strong men. Today Australia has become a Nanny State where everything is banned e.g.- it's illegal not to wear a helmet on a bike; it's illegal to chop down or prune trees on your own property. It's now a place where a city parking space might have 7-10 signs outlining a different set of parking laws for different timezones and days of the week. I could type forever.
Obviously I am looking for a neat wordpress designed blog with a focus on having a great banner that gives an indication of this change. From strong, determined individuals to a nation being forced to cower under a nanny. I'm open to your interpretation.
The blog title is "Loose Saltbush" with a byline of "what the bloody hell happened".

```html
<!DOCTYPE html>
<html lang="en">
<head>
<meta charset="utf-8">
<title>Loose Saltbush — What the bloody hell happened</title>
<link href="https://fonts.googleapis.com/css2?family=Open+Sans:ital,wght@0,400;0,600;0,700;0,800;1,400&display=swap" rel="stylesheet">
<style>
:root{
  --orange:#f7941d;
  --ink:#2f2f2f;
  --text:#555;
  --muted:#8a8a8a;
  --line:#e3e3e3;
  --page:#f5f6f9;
  --white:#fff;
  --dark:#333;
  --footer:#2c2c2c;
  --footer-text:#b9b9b9;
  --tweet:#1d9bd6;
}
*{box-sizing:border-box;margin:0;padding:0}
html,body{width:1200px;height:2675px;overflow:hidden}
body{position:relative;background:var(--page);font-family:"Open Sans",Arial,sans-serif;color:var(--text)}
.abs{position:absolute}
ul{list-style:none}

/* header */
.site-header{left:0;top:0;width:1200px;height:75px;background:var(--white);border-top:3px solid var(--orange);display:flex;align-items:center;justify-content:center;gap:12px}
.brand-mark{width:14px;height:14px;background:var(--orange)}
.brand-name{font-weight:700;font-size:30px;letter-spacing:1px;color:var(--ink)}

.main-nav{left:0;top:75px;width:1200px;height:48px;background:#f7f7f7;border-top:1px solid var(--line);border-bottom:1px solid var(--line)}
.main-nav ul{position:absolute;left:132px;top:-1px;display:flex;height:48px}
.main-nav li{height:48px;border-left:1px solid var(--line);font-size:12px;color:#333;display:flex;align-items:center;justify-content:center;text-transform:uppercase}
.main-nav li:last-child{border-right:1px solid var(--line)}
.main-nav li.is-active{background:var(--white);color:var(--orange);font-weight:700;border-bottom:3px solid var(--orange)}

/* hero */
.hero{left:0;top:123px;width:1200px;height:489px;background:linear-gradient(180deg,#a88d7a 0%,#c59068 22%,#6c6a70 45%,#3d5266 62%,#2c3f4d 100%)}
.hero-arrows{left:132px;top:478px;display:flex;gap:2px}
.hero-arrows span{width:38px;height:39px;background:var(--orange);display:flex;align-items:center;justify-content:center}
.hero-caption{left:132px;top:519px;width:938px;height:93px;display:flex}
.hero-caption .copy{width:838px;background:rgba(30,30,30,.78);padding:10px 12px}
.hero-caption h1{color:var(--white);font-size:26px;font-weight:800;letter-spacing:.5px;line-height:34px}
.hero-caption p{color:#eee;font-size:12px;line-height:19px}
.hero-caption .cta{width:100px;background:var(--orange);color:var(--white);font-weight:700;font-size:13px;display:flex;align-items:center;justify-content:center}

/* section titles */
.section-title{font-size:30px;font-weight:700;color:var(--ink);line-height:36px;text-transform:uppercase}

/* blog cards */
.post-card{left:132px;width:638px;height:239px;background:var(--white);border:1px solid var(--line);padding:0 12px}
.post-card h3{margin-top:12px;font-size:14px;font-weight:600;color:var(--ink);line-height:20px}
.meta{display:flex;gap:22px;font-size:11px;color:var(--muted);margin-top:8px;align-items:center}
.meta span{display:flex;align-items:center;gap:6px}
.meta i{display:inline-block;width:9px;height:9px;background:#aaa}
.post-card .body{display:flex;gap:22px;margin-top:18px}
.thumb{width:211px;height:143px;flex:none}
.post-card p{font-size:12px;line-height:23px;color:var(--text);width:385px;margin-top:-6px}
.btn-read{display:inline-block;margin-top:10px;background:var(--orange);color:var(--white);font-size:11px;font-weight:700;width:89px;height:27px;line-height:27px;text-align:center}

/* latest articles */
.articles{left:132px;top:1828px;width:638px;height:401px;background:var(--white);border:1px solid var(--line)}
.lead{position:absolute;left:12px;top:14px;width:298px}
.lead .img{width:298px;height:192px;background:linear-gradient(180deg,#0c1530 0%,#1a2750 55%,#3a3060 70%,#c08a3a 80%,#0d1a33 100%)}
.lead h3{margin-top:16px;font-size:14px;font-weight:700;color:var(--ink);line-height:22px}
.lead .by{margin-top:10px;display:flex;justify-content:space-between;font-size:11px;color:var(--muted)}
.lead .by b{color:var(--ink);font-weight:600;margin-right:14px}
.lead p{margin-top:16px;font-size:12px;line-height:23px}
.mini-list{position:absolute;left:336px;top:20px}
.mini-list li{display:flex;gap:16px;height:96px}
.mini-list .img{width:78px;height:71px;flex:none}
.mini-list h4{font-size:12px;font-weight:700;color:var(--ink);line-height:21px;width:200px}
.mini-list .meta{gap:16px;font-size:10px;margin-top:8px}

/* sidebar */
.widget-head{left:800px;width:268px;height:50px;background:var(--dark);color:var(--white);font-weight:700;font-size:18px;display:flex;align-items:center;justify-content:center;text-transform:uppercase}
.widget{left:800px;width:268px;background:var(--white);border:1px solid var(--line)}
.popular li{display:flex;gap:14px;height:96px;padding:0 12px}
.popular .img{width:82px;height:73px;flex:none}
.popular h4{font-size:11px;font-weight:700;color:var(--ink);line-height:20px;text-transform:uppercase;margin-top:2px;width:138px}
.popular .meta{gap:10px;font-size:10px;margin-top:4px}
.feature .img{margin:14px 8px 0;height:168px;background:linear-gradient(180deg,#1f3c78 0%,#4d6aa2 45%,#d08a3e 70%,#2b2f3c 100%)}
.feature h4{margin-top:18px;color:var(--orange);font-size:12px;font-weight:700;text-align:center;line-height:23px;text-transform:uppercase}
.feature p{font-size:12px;line-height:23px;text-align:center;padding:0 24px;margin-top:12px}
.categories li{display:flex;justify-content:space-between;align-items:center;height:30px;padding:0 22px 0 12px;font-size:11px}
.categories .label{display:flex;align-items:center;gap:10px}
.categories .dot{width:16px;height:16px;border:1px solid #bbb;border-radius:50%;display:flex;align-items:center;justify-content:center}
.tweets li{display:flex;gap:10px;padding:0 14px;height:112px}
.tweet-mark{width:14px;height:14px;border-radius:50%;background:var(--tweet);flex:none;margin-top:6px}
.tweets p{font-size:11px;font-style:italic;line-height:20px;color:var(--muted)}
.tweets p b{font-style:normal;font-weight:600;color:var(--ink)}
.tweets .handle{color:var(--tweet);font-style:normal}
.tweets .when{display:block;color:var(--tweet);font-style:normal;font-size:10px}

/* newsletter */
.newsletter{left:0;top:2314px;width:1200px;height:95px;background:var(--orange)}
.newsletter h2{position:absolute;left:225px;top:32px;color:var(--white);font-size:24px;font-weight:700;letter-spacing:.5px}
.newsletter .field{position:absolute;left:558px;top:27px;width:396px;height:43px;background:var(--white);font-size:12px;color:#555;padding:14px 14px}
.newsletter .submit{position:absolute;left:957px;top:27px;width:111px;height:43px;background:#1b1b1b;color:var(--white);font-weight:700;font-size:14px;display:flex;align-items:center;justify-content:center}

/* footer */
.site-footer{left:0;top:2409px;width:1200px;height:266px;background:var(--footer);color:var(--footer-text)}
.foot-col{position:absolute;top:32px}
.foot-col h5{color:var(--white);font-size:13px;font-weight:700;margin-bottom:10px;text-transform:uppercase}
.foot-col li{font-size:10px;line-height:19.3px;text-transform:uppercase;display:flex;align-items:center;gap:10px}
.foot-col li::before{content:"";width:3px;height:3px;background:var(--footer-text)}
.contact li{text-transform:none;font-size:11px;line-height:26px;align-items:flex-start}
.contact li::before{display:none}
.contact svg{flex:none;margin-top:8px}
.contact a{color:var(--footer-text);text-decoration:underline}
.follow p{font-size:11px;line-height:18px;width:220px}
.socials{display:flex;gap:10px;margin-top:18px}
.socials span{width:32px;height:32px;border:1px solid #777;border-radius:50%}
.copyright{position:absolute;left:0;top:2634px;width:1200px;text-align:center;font-size:11px;color:#8d8d8d}
</style>
</head>
<body>

<header class="site-header abs">
  <span class="brand-mark"></span>
  <span class="brand-name">LOOSE SALTBUSH</span>
</header>

<nav class="main-nav abs">
  <ul>
    <li class="is-active" style="width:105px">Home</li>
    <li style="width:146px">About Us</li>
    <li style="width:159px">Australia Today</li>
    <li style="width:168px">Recent Blog</li>
    <li style="width:157px">Testimonials</li>
    <li style="width:89px">FAQ</li>
    <li style="width:114px">Contact Us</li>
  </ul>
</nav>

<section class="hero abs" role="img" aria-label="Harbour city skyline at sunset with a steel arch bridge and moored boats"></section>
<div class="hero-arrows abs">
  <span><svg width="10" height="14" viewBox="0 0 10 14"><path d="M7 2 2 7l5 5" stroke="#fff" stroke-width="2" fill="none"/></svg></span>
  <span><svg width="10" height="14" viewBox="0 0 10 14"><path d="m3 2 5 5-5 5" stroke="#fff" stroke-width="2" fill="none"/></svg></span>
</div>
<div class="hero-caption abs">
  <div class="copy">
    <h1>WHAT THE BLOODY HELL HAPPENED</h1>
    <p>It is a long established fact that a reader will be distracted by the readable content of a page when looking at its layout. The point of using Lorem Ipsum is that it has a more-or-less normal distribution of letters, as opposed to look like readable English</p>
  </div>
  <div class="cta">CLICK HERE</div>
</div>

<h2 class="section-title abs" style="left:132px;top:651px">Recent Blog</h2>

<article class="post-card abs" style="top:710px">
  <h3>IT IS A LONG ESTABLISHED FACT THAT A READER WILL BE DISTRACTED</h3>
  <div class="meta"><span><i></i>Posted by admin</span><span><i></i>Nov 23, 2017</span><span><i></i>4 Comments</span><span><i></i>13</span></div>
  <div class="body">
    <div class="thumb" role="img" aria-label="Street protest with red flags" style="background:linear-gradient(135deg,#8a8f98,#b8323a 50%,#4b4f58)"></div>
    <div><p>It is a long established fact that a reader will be distracted by the dable content of a page when looking at its layout. The point of using Lorem are Ipsum is that it has a more-or-less normal distribution of letters, as posed to usingmaking it look like readable...</p><span class="btn-read">READ MORE</span></div>
  </div>
</article>

<article class="post-card abs" style="top:974px">
  <h3>IT IS A LONG ESTABLISHED FACT THAT A READER WILL BE DISTRACTED</h3>
  <div class="meta"><span><i></i>Posted by admin</span><span><i></i>Nov 23, 2017</span><span><i></i>4 Comments</span><span><i></i>13</span></div>
  <div class="body">
    <div class="thumb" role="img" aria-label="Police officer on a motorcycle in a city street" style="background:linear-gradient(180deg,#6b6050,#9a958c 55%,#5a5a5c)"></div>
    <div><p>It is a long established fact that a reader will be distracted by the dable content of a page when looking at its layout. The point of using Lorem are ipsum is that it has a more-or-less normal distribution of letters, as posed to usingmaking it look like readable...</p><span class="btn-read">READ MORE</span></div>
  </div>
</article>

<article class="post-card abs" style="top:1238px">
  <h3>IT IS A LONG ESTABLISHED FACT THAT A READER WILL BE DISTRACTED</h3>
  <div class="meta"><span><i></i>Posted by admin</span><span><i></i>Nov 23, 2017</span><span><i></i>4 Comments</span><span><i></i>13</span></div>
  <div class="body">
    <div class="thumb" role="img" aria-label="Rows of parked cars in the evening light" style="background:linear-gradient(160deg,#4b3c36,#b6423a 45%,#d9c8b8)"></div>
    <div><p>It is a long established fact that a reader will be distracted by the dable content of a page when looking at its layout. The point of using Lorem are Ipsum is that it has a more-or-less normal distribution of letters, as posed to usingmaking it look like readable...</p><span class="btn-read">READ MORE</span></div>
  </div>
</article>

<article class="post-card abs" style="top:1501px">
  <h3>IT IS A LONG ESTABLISHED FACT THAT A READER WILL BE DISTRACTED</h3>
  <div class="meta"><span><i></i>Posted by admin</span><span><i></i>Nov 23, 2017</span><span><i></i>4 Comments</span><span><i></i>13</span></div>
  <div class="body">
    <div class="thumb" role="img" aria-label="Festival dancers in red costumes under a blue sky" style="background:linear-gradient(180deg,#3f74c4,#7fa8d8 45%,#c8453a 70%,#6a8a3e)"></div>
    <div><p>It is a long established fact that a reader will be distracted by the dable content of a page when looking at its layout. The point of using Lorem are ipsum is that it has a more-or-less normal distribution of letters, as posed to usingmaking it look like readable...</p><span class="btn-read">READ MORE</span></div>
  </div>
</article>

<h2 class="section-title abs" style="left:132px;top:1774px">Latest Articles</h2>

<section class="articles abs">
  <div class="lead">
    <div class="img" role="img" aria-label="Fireworks over a harbour at night"></div>
    <h3>IT IS A LONG ESTABLISHED FACT THAT A READER WILL BE DISTRACTED</h3>
    <div class="by"><span><b>Tom Reddy</b>November 28, 2017</span><svg width="16" height="14" viewBox="0 0 16 14"><path d="M1 1h14v9H6l-3 3v-3H1z" fill="none" stroke="#999"/></svg></div>
    <p>It is a long established fact that a reader will be distrac ted by the readable content of a page when looking making it look like readable English.</p>
  </div>
  <ul class="mini-list">
    <li><div class="img" role="img" aria-label="Crowd at a street rally" style="background:linear-gradient(135deg,#7a6a5a,#b0a090)"></div><div><h4>IT IS A LONG ESTABLISHED FACT BY THE READABLE</h4><div class="meta"><span><i></i>NOV 03, 2017</span><span><i></i>4 COMMENTS</span></div></div></li>
    <li><div class="img" role="img" aria-label="Busy pedestrian crossing" style="background:linear-gradient(135deg,#5c5048,#a88c78)"></div><div><h4>IT IS A LONG ESTABLISHED FACT BY THE READABLE</h4><div class="meta"><span><i></i>NOV 03, 2017</span><span><i></i>4 COMMENTS</span></div></div></li>
    <li><div class="img" role="img" aria-label="Tropical beach with palm trees" style="background:linear-gradient(180deg,#4e9bd0,#8fc08a 55%,#d9c69a)"></div><div><h4>IT IS A LONG ESTABLISHED FACT BY THE READABLE</h4><div class="meta"><span><i></i>NOV 03, 2017</span><span><i></i>4 COMMENTS</span></div></div></li>
    <li><div class="img" role="img" aria-label="Traffic on a city road" style="background:linear-gradient(135deg,#6a6a70,#b5a8a0)"></div><div><h4>IT IS A LONG ESTABLISHED FACT BY THE READABLE</h4><div class="meta"><span><i></i>NOV 03, 2017</span><span><i></i>4 COMMENTS</span></div></div></li>
  </ul>
</section>

<div class="widget-head abs" style="top:658px">Popular Post</div>
<aside class="widget popular abs" style="top:708px;height:390px;padding-top:12px">
  <ul>
    <li><div class="img" role="img" aria-label="Opera house by the harbour" style="background:linear-gradient(180deg,#3b78c8,#d7a35a 70%,#3c4a5a)"></div><div><h4>It long established the readable</h4><div class="meta"><span><i></i>NOV 03, 2017</span><span><i></i>14</span></div></div></li>
    <li><div class="img" role="img" aria-label="City towers above a park" style="background:linear-gradient(180deg,#4f8fd0,#7a8a90 55%,#4e6a3c)"></div><div><h4>It long established the readable</h4><div class="meta"><span><i></i>NOV 03, 2017</span><span><i></i>14</span></div></div></li>
    <li><div class="img" role="img" aria-label="Friends smiling on the beach" style="background:linear-gradient(135deg,#c8a070,#e0c8a0 50%,#6aa0c0)"></div><div><h4>It long established the readable</h4><div class="meta"><span><i></i>NOV 03, 2017</span><span><i></i>14</span></div></div></li>
    <li><div class="img" role="img" aria-label="Kangaroos on a grassy field" style="background:linear-gradient(180deg,#4c6a2c,#7a9a3a 60%,#3c5020)"></div><div><h4>It long established the readable</h4><div class="meta"><span><i></i>NOV 03, 2017</span><span><i></i>14</span></div></div></li>
  </ul>
</aside>

<aside class="widget feature abs" style="top:1116px;height:421px">
  <div class="img" role="img" aria-label="Opera house and harbour bridge at dusk"></div>
  <h4>Cultural decay of everyday life<br>in Australia today</h4>
  <p>It is a long established fact that a reader will be distracted by the dable content of when looking at its layout.</p>
  <p style="margin-top:10px">The point of using Lorem are Ipsum is that it has a more-or-less normal bution of letters, as posed...</p>
</aside>

<div class="widget-head abs" style="top:1562px">Categories</div>
<aside class="widget categories abs" style="top:1612px;height:178px;padding-top:16px">
  <ul>
    <li><span class="label"><span class="dot"><svg width="6" height="8" viewBox="0 0 6 8"><path d="m1 1 3 3-3 3" stroke="#999" fill="none"/></svg></span>Coit is a long established</span><span>( 4 )</span></li>
    <li><span class="label"><span class="dot"><svg width="6" height="8" viewBox="0 0 6 8"><path d="m1 1 3 3-3 3" stroke="#999" fill="none"/></svg></span>It is a long established</span><span>( 5 )</span></li>
    <li><span class="label"><span class="dot"><svg width="6" height="8" viewBox="0 0 6 8"><path d="m1 1 3 3-3 3" stroke="#999" fill="none"/></svg></span>Lorem Ipsum Dummy</span><span>( 30 )</span></li>
    <li><span class="label"><span class="dot"><svg width="6" height="8" viewBox="0 0 6 8"><path d="m1 1 3 3-3 3" stroke="#999" fill="none"/></svg></span>It is a long established</span><span>( 41 )</span></li>
    <li><span class="label"><span class="dot"><svg width="6" height="8" viewBox="0 0 6 8"><path d="m1 1 3 3-3 3" stroke="#999" fill="none"/></svg></span>Lorem Ipsum Dummy</span><span>( 7 )</span></li>
  </ul>
</aside>

<div class="widget-head abs" style="top:1817px">Latest Tweet's</div>
<aside class="widget tweets abs" style="top:1867px;height:362px;padding-top:22px">
  <ul>
    <li><span class="tweet-mark"></span><p><span class="handle">@Loose Saltbush</span> t is a long established fact that a reader will be <b>distracted by the</b> when looking at its layout.<span class="when">2 month ago</span></p></li>
    <li><span class="tweet-mark"></span><p><span class="handle">@Loose Saltbush</span> t is a long established fact that a reader will be <b>distracted by the</b> when looking at its layout.<span class="when">2 month ago</span></p></li>
    <li><span class="tweet-mark"></span><p><span class="handle">@Loose Saltbush</span> t is a long established fact that a reader will be <b>distracted by the</b> when looking at its layout.<span class="when">2 month ago</span></p></li>
  </ul>
</aside>

<section class="newsletter abs">
  <svg class="abs" style="left:132px;top:16px" width="104" height="79" viewBox="0 0 104 79"><path d="M4 30 70 4l30 52-66 22z" fill="#e8861a"/><path d="M4 30 52 46 70 4" fill="none" stroke="#f7a84a" stroke-width="3"/></svg>
  <h2>SUBSCRIBE NEWSLETTER :</h2>
  <div class="field">Enter Your Email Id :</div>
  <div class="submit">SUBSCRIBE</div>
</section>

<footer class="site-footer abs">
  <div class="foot-col" style="left:130px">
    <h5>Quick Links</h5>
    <ul><li>Home</li><li>About Us</li><li>Australia Today</li><li>Recent Blog</li><li>Testimonials</li><li>FAQ</li><li>Contact Us</li></ul>
  </div>
  <div class="foot-col" style="left:337px">
    <h5>Informations</h5>
    <ul><li>Terms &amp; Conditions</li><li>Privacy Policy</li><li>Site Map</li><li>Disclaimer</li><li>Futured Blog</li><li>More Info</li></ul>
  </div>
  <div class="foot-col contact" style="left:574px">
    <h5>Contact Us</h5>
    <ul>
      <li><svg width="12" height="12" viewBox="0 0 12 12"><path d="M2 1h3l1 3-2 1a6 6 0 0 0 3 3l1-2 3 1v3c-6 0-10-4-9-9z" fill="var(--orange)"/></svg>(000)-555-0182 &nbsp;(Phone)</li>
      <li><svg width="12" height="12" viewBox="0 0 12 12"><rect x="1" y="3" width="10" height="7" fill="var(--orange)"/><rect x="3" y="0" width="6" height="3" fill="var(--orange)"/></svg>(000)-555-0183 &nbsp;(Fax)</li>
      <li><svg width="12" height="10" viewBox="0 0 12 10"><rect width="12" height="9" fill="var(--orange)"/><path d="m0 0 6 5 6-5" stroke="#2c2c2c" fill="none"/></svg><a>info@loosesaltbush.example</a></li>
      <li style="line-height:18px"><svg width="10" height="13" viewBox="0 0 10 13" style="margin-top:3px"><path d="M5 0a5 5 0 0 1 5 5c0 3-5 8-5 8S0 8 0 5a5 5 0 0 1 5-5z" fill="var(--orange)"/><circle cx="5" cy="5" r="2" fill="#2c2c2c"/></svg><span># lorem ipsum Dummy text<br>Lorem Ipsum</span></li>
    </ul>
  </div>
  <div class="foot-col follow" style="left:849px">
    <h5>Follow Us</h5>
    <p>It is a long established fact that a reader will be distracted by the content of a page when looking at its...</p>
    <div class="socials"><span></span><span></span><span></span><span></span></div>
  </div>
</footer>
<p class="copyright">©2017 Loose Saltbush | All rights reserved.</p>

</body>
</html>
```